I want a business card that is going to show a creative spark but without limiting me to an industry. Something edgy but that wont go out of date. I want it state My business name Serafina Loire, profession - Professional Makeup Artist contact number and email

My service is to provide makeup services from bridal, fashion, photography, film, TV and so on. It is creative and different so i want that to be reflected.

I would like the card double sided.
Updates

 I would LOVE a background on my card something like this image... i can supply an image to be formed like this

Please use the image uploaded

Can we try using the image provided on one side of the card and then writing and details on the other side

Target Market(s)

I am targeting a wide range of people from Creative directors to the individual eg. bride

Industry/Entity Type

Business

Requirements
Must have
• Name: Delphine Hartwell
contact numbe 0417853120
email address:info@serafinaloire.com
website: www.serafinaloire.com
One of the images attached

professional makeup artist / hair stylist

I want it to show creativity
Nice to have
• logo, Double-sided card
Should not have
• the design should not use tradional style. Or images that are not my own

```html
<!DOCTYPE html>
<html lang="en">
<head>
<meta charset="utf-8">
<title>Serafina Loire – Business Card, Front and Back</title>
<link rel="stylesheet" href="https://fonts.googleapis.com/css2?family=Kalam:wght@300;400&display=swap">
<style>
  :root {
    --page: #ffffff;
    --card-top: #f9e9f0;
    --card-mid: #ef9cc4;
    --card-bottom: #e0157f;
    --ink: #141414;
    --accent-ink: #7c1246;
    --art-dark: #2a1420;
    --art-rose: #c64a8a;
  }
  * { margin: 0; padding: 0; box-sizing: border-box; }
  html, body {
    width: 1200px; height: 1200px; overflow: hidden;
    background: var(--page);
  }
  .canvas { position: relative; width: 1200px; height: 1200px; }

  .card {
    position: absolute;
    background: linear-gradient(180deg, var(--card-top) 0%, var(--card-mid) 55%, var(--card-bottom) 100%);
    font-family: "Kalam", cursive;
    color: var(--ink);
    text-align: center;
  }
  .card--front { left: 15px; top: 8px; width: 780px; height: 585px; }
  .card--back  { left: 402px; top: 600px; width: 783px; height: 588px; }

  .brand-name {
    position: absolute; left: 0; right: 0; top: 14px;
    font-weight: 300; font-size: 86px; line-height: 1;
    letter-spacing: 2px;
  }
  .eye-art {
    position: absolute; left: 202px; top: 154px; width: 368px; height: 266px;
    border-radius: 50% 50% 45% 45%;
    background: radial-gradient(ellipse at 55% 55%, var(--art-dark) 0%, var(--art-rose) 55%, rgba(198,74,138,0) 72%);
    opacity: .55;
  }
  .profession {
    position: absolute; left: 112px; right: 113px; top: 420px;
    font-size: 40px; line-height: 1.1; color: var(--accent-ink);
    padding-bottom: 4px;
    border-bottom: 3px solid var(--ink);
  }
  .contact {
    position: absolute; left: 0; right: 0;
    font-size: 31px; line-height: 1; color: var(--accent-ink);
    font-weight: 300; white-space: pre;
  }
  .contact--phone { top: 480px; padding-left: 12px; }
  .contact--email { top: 528px; }

  .services {
    position: absolute; left: 0; right: 0; top: 34px;
    font-size: 37px; line-height: 49px; font-weight: 300;
    list-style: none;
  }
  .services__title { display: block; }
  .lips-art {
    position: absolute; left: 190px; top: 337px; width: 405px; height: 205px;
    border-radius: 48% 48% 50% 50% / 40% 40% 60% 60%;
    background: radial-gradient(ellipse at 50% 50%, var(--art-dark) 0%, var(--art-rose) 50%, rgba(198,74,138,0) 72%);
    opacity: .6;
  }
</style>
</head>
<body>
<main class="canvas">
  <section class="card card--front" aria-label="Card front">
    <h1 class="brand-name">Serafina Loire</h1>
    <div class="eye-art" role="img" aria-label="Brush-drawn illustration of a closed eye with brow and long lashes"></div>
    <p class="profession">Professional Make up Artist</p>
    <p class="contact contact--phone">Phone:  0417-853-120</p>
    <p class="contact contact--email">e-mail:    serafinaloire@studiomail.com.au</p>
  </section>

  <section class="card card--back" aria-label="Card back">
    <ul class="services">
      <li class="services__title">Make up Services include:</li>
      <li>Wedding</li>
      <li>Fashion</li>
      <li>Photography</li>
      <li>Film</li>
      <li>Television</li>
    </ul>
    <div class="lips-art" role="img" aria-label="Painted illustration of lips in dark ink and rose"></div>
  </section>
</main>
</body>
</html>
```